Landing Page Design

This project needs landing page desing only. However, whoever wins this round will get to work directly on all other pages of the website as a separate private project.

See attached file for more details.

Target Market(s)

25-60 year old person who is looking for health insurance quotes.

Industry/Entity Type

Health Insurance

Number of Pages Required

1 page

Font styles to use
Sans Serif

Requirements
Must have
• see attachment
Nice to have
• see attachment
Should not have
• see attachment

```html
<!DOCTYPE html>
<html lang="en">
<head>
<meta charset="utf-8">
<title>CoverWiseRates.com – Compare Health Insurance Plans</title>
<link href="https://fonts.googleapis.com/css2?family=Open+Sans:wght@300;400;600;700;800&display=swap" rel="stylesheet">
<style>
:root{
  --navy:#0b2f63;
  --navy-dark:#08264f;
  --red:#c8171d;
  --red-dark:#a51014;
  --teal-ink:#0f4a66;
  --rust:#b8321f;
  --ink:#444;
  --muted:#666;
  --row-light:#f7f7f7;
  --row-dark:#e6e6e6;
  --gray-band:#e6e6e6;
  --line:#c9c9c9;
  --white:#fff;
}
*{box-sizing:border-box;margin:0;padding:0}
html,body{width:1092px;height:1200px;overflow:hidden}
body{font-family:'Open Sans',sans-serif;color:var(--ink);background:var(--white);position:relative}

/* header */
.site-header{position:absolute;top:0;left:0;width:1092px;height:66px;background:var(--navy);color:var(--white)}
.brand{position:absolute;left:92px;top:14px;display:flex;align-items:center;gap:8px}
.brand-mark{width:26px;height:26px;border-radius:50%;background:var(--white)}
.brand-name{font-size:20px;font-weight:700;letter-spacing:-.2px}
.main-nav{position:absolute;left:408px;top:24px;display:flex;gap:0;font-size:13px}
.main-nav a{color:var(--white);text-decoration:none;margin-right:49px}
.header-call{position:absolute;left:767px;top:16px;display:flex;align-items:center;gap:9px;font-size:13.5px}
.call-icon{width:32px;height:32px;border-radius:50%;background:var(--red);display:flex;align-items:center;justify-content:center}
.header-call strong{font-weight:700}

/* hero */
.hero{position:absolute;top:66px;left:0;width:1092px;height:429px;overflow:hidden}
.hero-photo{position:absolute;inset:0;background:linear-gradient(90deg,#f1efee 0%,#ece8e4 45%,#e3d6cb 62%,#cfc1b3 80%,#d8cfc6 100%)}
.hero-title{position:absolute;left:83px;top:97px;font-weight:700;line-height:1.25}
.hero-title .line-1{font-size:27px;color:var(--teal-ink)}
.hero-title .line-2{font-size:29px;color:var(--rust)}
.quote-box{position:absolute;left:83px;top:179px;width:432px;height:147px;background:var(--navy);border-radius:16px;color:var(--white)}
.quote-box h2{font-weight:300;font-size:23px;text-align:center;margin-top:26px;letter-spacing:-.2px}
.quote-box h2 b{font-weight:800}
.zip-form{position:absolute;left:23px;top:69px;width:387px;height:38px;background:var(--white);border-radius:19px}
.zip-form span{position:absolute;left:18px;top:10px;font-size:13px;color:#777}
.see-plans{position:absolute;right:2px;top:2px;width:128px;height:34px;border-radius:17px;background:linear-gradient(#d9262a,var(--red-dark));color:var(--white);font-weight:700;font-size:13px;display:flex;align-items:center;justify-content:center;gap:7px}
.partners{position:absolute;left:113px;top:340px;width:342px;height:37px;background:var(--white);display:flex;align-items:center;justify-content:space-around;padding:0 10px}
.partner-badge{height:20px;background:#9a9a9a;border-radius:3px}
.slider-dots{position:absolute;left:523px;top:401px;display:flex;gap:4px}
.slider-dots i{width:9px;height:9px;border-radius:50%;background:#4f6d96}
.slider-dots i.active{background:var(--red)}

/* call bands */
.band{position:absolute;top:495px;height:121px;width:546px;color:var(--white)}
.band-phone{left:0;background:linear-gradient(90deg,#0f3671,#0b2f63)}
.band-phone .lead{position:absolute;left:85px;top:23px;font-size:16px;font-weight:300}
.band-phone .lead b{font-size:22px;font-weight:700}
.band-phone p{position:absolute;left:86px;top:54px;width:400px;font-size:13px;line-height:23px}
.band-state{left:546px;background:linear-gradient(90deg,#c3161c,#d0262a)}
.band-state .l1{position:absolute;left:86px;top:31px;font-size:18px;font-weight:300}
.band-state .l2{position:absolute;left:86px;top:57px;font-size:16px;font-weight:300}
.band-state .l2 b{font-size:24px;font-weight:700}

/* plan tables */
.plans h2{position:absolute;top:658px;font-size:21px;font-weight:700;color:var(--navy)}
.plan-table{position:absolute;top:703px;width:436px;border-collapse:collapse;font-size:10.5px}
.plan-table th{height:40px;background:linear-gradient(#10428a,var(--navy));color:var(--white);font-size:13px;font-weight:700;text-align:center;border-right:1px solid #2d5796}
.plan-table th:first-child{text-align:left;padding-left:17px}
.plan-table td{height:32px;text-align:center;border:1px solid var(--line);color:#555}
.plan-table td:first-child{text-align:left;padding-left:17px}
.plan-table tr:nth-child(odd) td{background:var(--row-light)}
.plan-table tr:nth-child(even) td{background:var(--row-dark)}
.types{left:90px}
.tiers{left:558px}

/* faq */
.faq{position:absolute;top:922px;left:0;width:1092px;height:217px;background:var(--gray-band)}
.faq-item{position:absolute;top:54px;width:260px}
.faq-item h3{font-size:13.5px;font-weight:700;color:var(--navy);line-height:22px;margin-bottom:3px}
.faq-item p{font-size:10.5px;line-height:21px;color:var(--muted);padding-left:2px}
.faq-item a{color:var(--navy);text-decoration:none}
.divider{position:absolute;top:55px;width:1px;height:106px;background:#c8c8c8}

/* footer */
.site-footer{position:absolute;top:1139px;left:0;width:1092px;height:61px;background:var(--navy);color:var(--white);font-size:10.5px}
.footer-links{position:absolute;left:91px;top:24px;display:flex;gap:0}
.footer-links span{margin-right:22px}
.follow{position:absolute;left:827px;top:17px;display:flex;align-items:center;gap:8px}
.social{width:24px;height:24px;border-radius:50%}
</style>
</head>
<body>

<header class="site-header">
  <div class="brand"><span class="brand-mark"></span><span class="brand-name">CoverWiseRates.com</span></div>
  <nav class="main-nav"><a href="#">Home</a><a href="#">About us</a><a href="#">Plans</a><a href="#">Contact us</a></nav>
  <div class="header-call">
    <span class="call-icon"><svg width="14" height="14" viewBox="0 0 24 24"><path fill="#fff" d="M6.6 10.8a15 15 0 006.6 6.6l2.2-2.2c.3-.3.7-.4 1-.2 1.1.4 2.3.6 3.6.6.6 0 1 .4 1 1V20c0 .6-.4 1-1 1A17 17 0 013 4c0-.6.4-1 1-1h3.5c.6 0 1 .4 1 1 0 1.3.2 2.5.6 3.6.1.3 0 .7-.2 1z"/></svg></span>
    <span>Call for Quotes : <strong>(800) 555-0199</strong></span>
  </div>
</header>

<section class="hero">
  <div class="hero-photo" role="img" aria-label="Photo of a smiling senior couple sitting together at home, over a faint flag and star backdrop"></div>
  <h1 class="hero-title"><span class="line-1">COMPARE 2016</span><br><span class="line-2">HEALTH INSURANCE PLANS</span></h1>
  <div class="quote-box">
    <h2>GET YOUR <b>FREE QUOTES</b> NOW!</h2>
    <div class="zip-form"><span>Enter zipcode</span>
      <div class="see-plans">SEE PLANS <svg width="7" height="10" viewBox="0 0 7 10"><path d="M1 1l4 4-4 4" stroke="#fff" stroke-width="2" fill="none"/></svg></div>
    </div>
  </div>
  <div class="partners">
    <span class="partner-badge" style="width:68px"></span>
    <span class="partner-badge" style="width:50px"></span>
    <span class="partner-badge" style="width:76px"></span>
    <span class="partner-badge" style="width:80px"></span>
  </div>
  <div class="slider-dots"><i class="active"></i><i></i><i></i><i></i></div>
</section>

<section class="band band-phone">
  <div class="lead">To shop over the phone <b>Call 1-800-555-0199</b></div>
  <p>Speak with a licensed agent and get expert advice on choosing a plan that's right for you</p>
</section>
<section class="band band-state">
  <div class="l1">Click your state below to get</div>
  <div class="l2"><b>free health insurance</b> quotes &amp; save!</div>
</section>

<section class="plans">
  <h2 style="left:90px">Health Insurance Plan Types</h2>
  <table class="plan-table types">
    <tr><th style="width:208px">Plan Types</th><th>PPO</th><th>EPO</th><th>POS</th><th>HMO</th></tr>
    <tr><td>PCP Required?</td><td>No</td><td>No</td><td>Yes</td><td>Yes</td></tr>
    <tr><td>Referrals Required</td><td>No</td><td>No</td><td>Yes</td><td>Yes</td></tr>
    <tr><td>Pre-Authorization Required?</td><td>Yes</td><td>Yes</td><td>No</td><td>Yes</td></tr>
    <tr><td>Quit-of-network Coverage?</td><td>Yes</td><td>No</td><td>Yes</td><td>No</td></tr>
  </table>

  <h2 style="left:558px">Health Insurance Plan Tiers</h2>
  <table class="plan-table tiers">
    <tr><th style="width:130px">Plan Types</th><th>PPO</th><th></th><th>EPO</th><th>POS</th><th>HMO</th></tr>
    <tr><td>Coverage Level</td><td>60%</td><td>70%</td><td colspan="2">80%</td><td>90%</td></tr>
    <tr><td>Prmium Level</td><td>Lowest</td><td>2nd Lowest</td><td colspan="2">2nd Highest</td><td>Highest</td></tr>
    <tr><td>Deductible</td><td>Highest</td><td>Moderate</td><td colspan="2">None</td><td>None</td></tr>
    <tr><td>Cost-Sharing</td><td>None</td><td>Yes</td><td colspan="2">None</td><td>None</td></tr>
  </table>
</section>

<section class="faq">
  <article class="faq-item" style="left:90px">
    <h3>How do I Buy Health Insurance?</h3>
    <p>For some, buying health insurance can be a confusing and overwhelming process. First, you have to find a health insurance plan within your budget... <a href="#">[ Read More ]</a></p>
  </article>
  <span class="divider" style="left:363px"></span>
  <article class="faq-item" style="left:410px">
    <h3>What is the Healthcare Marketplace?</h3>
    <p>The passage of the Affordable Care Act established the Healthcare Marketplace. There are two distinct divisions - a state level, and a federal level... <a href="#">[ Read More ]</a></p>
  </article>
  <span class="divider" style="left:690px"></span>
  <article class="faq-item" style="left:733px">
    <h3>What's the<br>"Health Insurance Exchange"?</h3>
    <p>The Health Insurance Exchange is the pool of health care plans and providers which are cooperating with the federal... <a href="#">[ Read More ]</a></p>
  </article>
  <span class="divider" style="left:1002px"></span>
</section>

<footer class="site-footer">
  <div class="footer-links">
    <span>Copyright © 2015. CoverWiseRates.com. All rights reserved.</span><span>/</span>
    <span>Partners</span><span>/</span><span>Privacy Policy</span><span>/</span><span>Terms of Use</span>
  </div>
  <div class="follow">
    <span>Follow Us :</span>
    <span class="social" style="background:#2f5fa8"></span>
    <span class="social" style="background:#3a9ad9"></span>
    <span class="social" style="background:#3b3b3b"></span>
    <span class="social" style="background:#1f7a9c"></span>
  </div>
</footer>

</body>
</html>
```